Rack Card for Willow Bend Dog Training

I love the logo you designed for me a while back (I had it updated and have the new files).

I need a rack card designed, 2 sided.

One side will be Willow Bend Dog Training (my general dog training business)

The other side will be my Deaf and Blind Dog Training Business speciality.

Both sides Full Color/4 color

3.5 x 8.5 inches

I can provide photos and text accordingly.

Let me know the estimated price and Turn around time.

```html
<!DOCTYPE html>
<html lang="en">
<head>
<meta charset="utf-8">
<title>Willow Bend Dog Training – Rack Card</title>
<link href="https://fonts.googleapis.com/css2?family=Poppins:wght@400;500;600;700;800&display=swap" rel="stylesheet">
<style>
:root{
  --stage:#bdbdbd;
  --ink:#3a3935;
  --cream:#efebdf;
  --paper:#ffffff;
  --rule:#8a877f;
  --photo-warm:#b7865a;
  --photo-cool:#9fb0b8;
  --photo-green:#8fa36a;
}
*{margin:0;padding:0;box-sizing:border-box}
html,body{width:1200px;height:2186px;overflow:hidden}
body{background:var(--stage);font-family:"Poppins",sans-serif;color:var(--ink);position:relative}
.card{position:absolute;top:437px;width:540px;height:1312px;background:var(--cream);overflow:hidden;box-shadow:0 18px 40px rgba(0,0,0,.35)}
.card--general{left:40px}
.card--special{left:620px}
.card__bg{position:absolute;inset:0;width:540px;height:1312px}
.abs{position:absolute}
.brand{left:30px;top:60px;display:flex;align-items:center;gap:10px}
.brand__dot{width:34px;height:34px;border:2px solid var(--ink);border-radius:50%}
.brand__name{font-size:24px;font-weight:500;color:var(--ink)}
.headline{left:28px;font-size:36px;line-height:1.02;font-weight:400;color:var(--ink);letter-spacing:-.3px}
.headline b{font-weight:800}
.photo{background:linear-gradient(160deg,var(--photo-warm),#5c4a3a)}
.photo--cutout{background:linear-gradient(180deg,#fff 0%,#e6e1d6 100%)}
.photo--circle{border-radius:50%;border:6px solid var(--ink)}
.section-title{font-size:19px;font-weight:700;line-height:1.15;padding-bottom:4px;border-bottom:1.5px solid var(--rule)}
.bullets{list-style:none;font-size:14.5px;line-height:1.2;color:var(--ink)}
.bullets li{position:relative;padding-left:24px;margin-bottom:10px}
.bullets li::before{content:"";position:absolute;left:2px;top:4px;width:10px;height:10px;border-radius:50%;background:var(--ink)}
.bullets li.plain::before{display:none}
.bullets--tight li{margin-bottom:2px}
.service-panel{left:278px;top:437px;width:232px;height:440px;background:var(--ink);border-radius:12px;color:var(--paper)}
.service-panel__head{position:absolute;left:16px;top:-6px;width:200px;height:88px;background:var(--cream);border:2px solid var(--ink);clip-path:polygon(0 0,100% 0,100% 82%,50% 100%,0 82%);text-align:center;padding-top:16px;color:var(--ink);font-weight:700;line-height:1.05}
.service-panel__head span{display:block;font-size:18px}
.service-panel__head strong{display:block;font-size:22px;font-weight:800}
.services{position:absolute;left:14px;top:104px;width:204px;list-style:none}
.services li{display:flex;align-items:center;gap:10px;height:49px;border-bottom:1px solid #5a5852;font-size:14.5px;font-weight:600}
.services li:last-child{border-bottom:none}
.services svg{width:30px;height:30px;flex:none}
.cta{left:28px;top:1105px;color:var(--paper);font-size:24px;line-height:1.1;font-weight:400}
.cta b{font-weight:800}
.contacts{left:28px;top:1170px;color:var(--paper);font-size:13px;line-height:1.5}
.contacts .row{display:flex;align-items:center;gap:6px}
.contacts .phone{font-size:15px;font-weight:700}
.contacts .gap{height:14px}
.contacts svg{width:14px;height:14px;flex:none}
.trainer{left:222px;top:1198px;color:var(--paper);font-size:20px;line-height:1.02;font-weight:800}
.trainer span{display:block;font-weight:400;font-size:18px;margin-top:3px}
.trainer-photo{left:372px;top:1035px;width:168px;height:277px;background:linear-gradient(170deg,#8a6a4e,#3f3a36 70%);border-radius:80px 80px 0 0}
</style>
</head>
<body>

<!-- General training side -->
<section class="card card--general" aria-label="Willow Bend Dog Training rack card, general side">
  <svg class="card__bg" viewBox="0 0 540 1312" aria-hidden="true">
    <path fill="var(--paper)" d="M0,0H540V385C460,410 360,400 280,362C190,322 90,310 0,330Z"/>
    <path fill="var(--ink)" d="M0,330C90,310 190,322 280,362C360,400 460,410 540,385V398C460,425 360,418 280,385C190,348 90,336 0,348Z"/>
    <path fill="var(--ink)" d="M0,975C100,950 200,995 300,965C400,935 470,900 540,890V1312H0Z"/>
  </svg>

  <div class="abs brand"><span class="brand__dot"></span><span class="brand__name">Willow Bend</span></div>
  <h1 class="abs headline" style="top:175px">DOG <b>TRAINING</b><br><b>&amp; BEHAVIORAL</b><br>SERVICES</h1>
  <div class="abs photo photo--cutout" role="img" aria-label="Tricolour shepherd dog sitting, cut out on white" style="left:315px;top:45px;width:215px;height:290px;border-radius:40% 40% 10% 10%"></div>

  <h2 class="abs section-title" style="left:30px;top:365px;width:212px">WE TEACH<br>OWNERS HOW TO</h2>
  <ul class="abs bullets" style="left:28px;top:430px;width:230px">
    <li>We teach dogs of all ages: Puppies, Adolescents &amp; Adults.</li>
    <li>Become the “Pack Guardian”. Read your dog’s signals (body language, signs of anxiety, etc.) and how to motivate him.</li>
    <li>Use structured play and games to obtain desired behavior and have fun with your dog.</li>
    <li>Good manners – what all good dogs should know.</li>
    <li>Proper leash and obedience skills (no pulling or lunging).</li>
    <li>How to handle ‘real-world experiences’ (skateboards, loud noises, meet and greet new people and dogs, etc.).</li>
  </ul>

  <div class="abs service-panel">
    <div class="service-panel__head"><span>WILLOW BEND</span><strong>DOG TRAINING</strong></div>
    <ul class="services">
      <li><svg viewBox="0 0 30 30"><circle cx="15" cy="15" r="14" fill="var(--paper)"/><circle cx="15" cy="15" r="6" fill="none" stroke="var(--ink)" stroke-width="2"/></svg>Puppy Training</li>
      <li><svg viewBox="0 0 30 30"><circle cx="15" cy="15" r="14" fill="var(--paper)"/><rect x="9" y="9" width="12" height="12" fill="none" stroke="var(--ink)" stroke-width="2"/></svg>House Breaking</li>
      <li><svg viewBox="0 0 30 30"><circle cx="15" cy="15" r="14" fill="var(--paper)"/><path d="M9 20L21 10" stroke="var(--ink)" stroke-width="2"/></svg>Leash Training</li>
      <li><svg viewBox="0 0 30 30"><circle cx="15" cy="15" r="14" fill="var(--paper)"/><path d="M9 15l4 4 8-8" fill="none" stroke="var(--ink)" stroke-width="2"/></svg>Obedience</li>
      <li><svg viewBox="0 0 30 30"><circle cx="15" cy="15" r="14" fill="var(--paper)"/><path d="M15 21s-6-4-6-8a3 3 0 0 1 6-1 3 3 0 0 1 6 1c0 4-6 8-6 8z" fill="none" stroke="var(--ink)" stroke-width="2"/></svg>Rescue Dog Training</li>
      <li><svg viewBox="0 0 30 30"><circle cx="15" cy="15" r="14" fill="var(--paper)"/><path d="M10 15h10M15 10v10" stroke="var(--ink)" stroke-width="2"/></svg>Separation Anxiety</li>
      <li><svg viewBox="0 0 30 30"><circle cx="15" cy="15" r="14" fill="var(--paper)"/><circle cx="11" cy="15" r="3" fill="var(--ink)"/><circle cx="19" cy="15" r="3" fill="var(--ink)"/></svg>Socialization</li>
    </ul>
  </div>

  <div class="abs photo photo--circle" role="img" aria-label="Beagle standing on green grass" style="left:28px;top:960px;width:118px;height:118px;background:linear-gradient(180deg,#c9d9a0,var(--photo-green))"></div>
  <div class="abs photo photo--circle" role="img" aria-label="Red-brown hound portrait" style="left:152px;top:988px;width:118px;height:118px"></div>
  <div class="abs photo photo--circle" role="img" aria-label="Happy mixed-breed dog with tongue out" style="left:272px;top:932px;width:118px;height:118px;background:linear-gradient(160deg,var(--photo-cool),#6a5a48)"></div>
  <div class="abs photo photo--circle" role="img" aria-label="Brown puppy resting on a blanket" style="left:394px;top:900px;width:118px;height:118px;background:linear-gradient(160deg,#dfe6ee,var(--photo-warm))"></div>

  <div class="abs trainer-photo" role="img" aria-label="Lead trainer kneeling with a shepherd dog"></div>
  <p class="abs cta">SCHEDULE <b>FREE 15 MINUTE</b><br>PHONE CONSULTATION</p>
  <div class="abs contacts">
    <div class="row"><svg viewBox="0 0 14 14"><path d="M7 1a4 4 0 0 1 4 4c0 3-4 8-4 8S3 8 3 5a4 4 0 0 1 4-4z" fill="none" stroke="currentColor" stroke-width="1.5"/><circle cx="7" cy="5" r="1.4" fill="currentColor"/></svg>LOS ANGELES</div>
    <div class="row phone"><svg viewBox="0 0 14 14"><circle cx="7" cy="7" r="6.3" fill="none" stroke="currentColor" stroke-width="1.4"/><path d="M4.5 4.2l1.4-.4.8 1.8-.9.7a5 5 0 0 0 1.9 1.9l.7-.9 1.8.8-.4 1.4C7.5 9.8 4.2 6.5 4.5 4.2z" fill="currentColor"/></svg>(310) 555-0142</div>
    <div class="gap"></div>
    <div class="row"><svg viewBox="0 0 14 14"><path d="M7 1a4 4 0 0 1 4 4c0 3-4 8-4 8S3 8 3 5a4 4 0 0 1 4-4z" fill="none" stroke="currentColor" stroke-width="1.5"/><circle cx="7" cy="5" r="1.4" fill="currentColor"/></svg>ORANGE COUNTY</div>
    <div class="row phone"><svg viewBox="0 0 14 14"><circle cx="7" cy="7" r="6.3" fill="none" stroke="currentColor" stroke-width="1.4"/><path d="M4.5 4.2l1.4-.4.8 1.8-.9.7a5 5 0 0 0 1.9 1.9l.7-.9 1.8.8-.4 1.4C7.5 9.8 4.2 6.5 4.5 4.2z" fill="currentColor"/></svg>(714) 555-0187</div>
  </div>
  <p class="abs trainer">DANA WHITFIELD<br>REYES<span>Lead Trainer</span></p>
</section>

<!-- Deaf and blind specialty side -->
<section class="card card--special" aria-label="Willow Bend deaf and blind dog training rack card">
  <svg class="card__bg" viewBox="0 0 540 1312" aria-hidden="true">
    <path fill="var(--paper)" d="M0,0H540V322C470,345 390,340 310,316C210,286 100,272 0,282Z"/>
    <path fill="var(--ink)" d="M0,282C100,272 210,286 310,316C390,340 470,345 540,322V334C470,358 390,354 310,330C210,300 100,290 0,296Z"/>
    <path fill="var(--ink)" d="M0,1035C120,995 250,1055 380,1020C450,1000 500,985 540,978V1312H0Z"/>
  </svg>

  <div class="abs brand"><span class="brand__dot"></span><span class="brand__name">Willow Bend</span></div>
  <h1 class="abs headline" style="top:163px;font-size:31px">WE SPECIALIZE IN<br><b>DEAF AND BLIND</b><br><b>DOG TRAINING</b></h1>
  <div class="abs photo photo--cutout" role="img" aria-label="Beagle sitting, cut out on white" style="left:285px;top:40px;width:245px;height:265px;border-radius:40% 40% 10% 10%"></div>

  <h2 class="abs section-title" style="left:30px;top:334px;width:214px">DEAF DOG TRAINING</h2>
  <ul class="abs bullets bullets--tight" style="left:28px;top:368px;width:272px">
    <li>Deaf dogs can easily be trained using hand signals.</li>
    <li>We owe it to our dogs to teach them how to behave, and that the world is a safe place.</li>
    <li>A dog with special needs is no exception.</li>
    <li class="plain">Training a dog that is deaf can come with it challenges.</li>
  </ul>
  <div class="abs photo photo--circle" role="img" aria-label="Border collie smiling on a beach" style="left:319px;top:383px;width:160px;height:160px;background:linear-gradient(180deg,var(--photo-cool),#d9cdb5)"></div>

  <div class="abs photo photo--circle" role="img" aria-label="Senior golden retriever portrait" style="left:34px;top:561px;width:160px;height:160px"></div>
  <h2 class="abs section-title" style="left:210px;top:571px;width:212px">BLIND DOG TRAINING</h2>
  <ul class="abs bullets bullets--tight" style="left:208px;top:605px;width:300px">
    <li>Deaf dogs can easily be trained using sound signals.</li>
    <li>A dog with special needs is no exception.</li>
    <li>Owners can wear a jingling bell, so your blind dog can find you.</li>
    <li class="plain">Blind Dogs have EXTREMELY heightened senses (especially smell and sound).</li>
  </ul>

  <h2 class="abs section-title" style="left:30px;top:784px;width:272px">DEAF / BLIND DOG TRAINING</h2>
  <ul class="abs bullets bullets--tight" style="left:28px;top:818px;width:262px">
    <li>Deaf/Blind dogs can easily be trained using touch and tactile cues.</li>
    <li>A dog with special needs is no exception.</li>
    <li>Training a dog that is both blind and deaf can come with its own challenges, we have many years of experience to help.</li>
  </ul>
  <div class="abs photo photo--circle" role="img" aria-label="White dog in a blue vest among trees" style="left:319px;top:789px;width:160px;height:160px;background:linear-gradient(160deg,var(--photo-green),#e8e6e0)"></div>

  <div class="abs trainer-photo" role="img" aria-label="Lead trainer kneeling with a shepherd dog"></div>
  <p class="abs cta">SCHEDULE <b>FREE 15 MINUTE</b><br>PHONE CONSULTATION</p>
  <div class="abs contacts">
    <div class="row"><svg viewBox="0 0 14 14"><path d="M7 1a4 4 0 0 1 4 4c0 3-4 8-4 8S3 8 3 5a4 4 0 0 1 4-4z" fill="none" stroke="currentColor" stroke-width="1.5"/><circle cx="7" cy="5" r="1.4" fill="currentColor"/></svg>LOS ANGELES</div>
    <div class="row phone"><svg viewBox="0 0 14 14"><circle cx="7" cy="7" r="6.3" fill="none" stroke="currentColor" stroke-width="1.4"/><path d="M4.5 4.2l1.4-.4.8 1.8-.9.7a5 5 0 0 0 1.9 1.9l.7-.9 1.8.8-.4 1.4C7.5 9.8 4.2 6.5 4.5 4.2z" fill="currentColor"/></svg>(310) 555-0142</div>
    <div class="gap"></div>
    <div class="row"><svg viewBox="0 0 14 14"><path d="M7 1a4 4 0 0 1 4 4c0 3-4 8-4 8S3 8 3 5a4 4 0 0 1 4-4z" fill="none" stroke="currentColor" stroke-width="1.5"/><circle cx="7" cy="5" r="1.4" fill="currentColor"/></svg>ORANGE COUNTY</div>
    <div class="row phone"><svg viewBox="0 0 14 14"><circle cx="7" cy="7" r="6.3" fill="none" stroke="currentColor" stroke-width="1.4"/><path d="M4.5 4.2l1.4-.4.8 1.8-.9.7a5 5 0 0 0 1.9 1.9l.7-.9 1.8.8-.4 1.4C7.5 9.8 4.2 6.5 4.5 4.2z" fill="currentColor"/></svg>(714) 555-0187</div>
  </div>
  <p class="abs trainer">DANA WHITFIELD<br>REYES<span>Lead Trainer</span></p>
</section>

</body>
</html>
```